Business Card Design

we need a business card design and logo for a new cleaning company ,called brightwater cleaning Service,LLC .we provide cleaning services
Updates

i will also like to include the company's website in the business card   brightwatercleaningservice.example

Industry/Entity Type

Business

Contact Information for Business Card

Brightwater Cleaning Service,LLC
Marco Villanueva
Owner
marco@brightwatercleaningservice.example
Cell 555-318-7724
Office 555-374-6082

```html
<!DOCTYPE html>
<html lang="en">
<head>
<meta charset="utf-8">
<title>Brightwater Cleaning Service – Business Card</title>
<link rel="stylesheet" href="https://fonts.googleapis.com/css2?family=Open+Sans:wght@400;600;700&family=Petit+Formal+Script&display=swap">
<style>
  :root {
    --card-white: #ffffff;
    --leaf-green: #8dc63f;
    --earth-brown: #5a3512;
    --ink: #1a1a1a;
    --page: #ececec;
  }
  * { margin: 0; padding: 0; box-sizing: border-box; }
  html, body {
    width: 1200px;
    height: 732px;
    overflow: hidden;
    background: var(--page);
  }
  .card {
    position: relative;
    width: 1200px;
    height: 732px;
    background: var(--card-white);
    overflow: hidden;
    font-family: "Open Sans", Arial, sans-serif;
    color: var(--ink);
  }
  .card__wave {
    position: absolute;
    inset: 0;
    width: 1200px;
    height: 732px;
  }
  .card__wave path { fill: var(--leaf-green); }

  .brand {
    position: absolute;
    left: 48px;
    top: 50px;
    display: flex;
    align-items: center;
    gap: 22px;
  }
  .brand__mark {
    width: 96px;
    height: 96px;
    background: var(--leaf-green);
    flex: none;
  }
  .brand__name {
    font-weight: 600;
    color: var(--earth-brown);
    text-transform: uppercase;
    line-height: 1.05;
  }
  .brand__name-main {
    display: block;
    font-size: 56px;
    letter-spacing: 3px;
  }
  .brand__name-sub {
    display: block;
    font-size: 36px;
    letter-spacing: 1px;
  }

  .person {
    position: absolute;
    left: 0;
    width: 420px;
    top: 362px;
    text-align: center;
    font-size: 30px;
    letter-spacing: 1.5px;
    line-height: 1.3;
  }
  .divider {
    position: absolute;
    left: 429px;
    top: 333px;
    width: 4px;
    height: 147px;
    background: var(--ink);
  }
  .contact {
    position: absolute;
    left: 472px;
    top: 340px;
    list-style: none;
    font-size: 27px;
    letter-spacing: 1.2px;
    line-height: 40px;
  }

  .tagline {
    position: absolute;
    left: 0;
    width: 1200px;
    top: 618px;
    text-align: center;
    font-family: "Petit Formal Script", cursive;
    font-size: 24px;
    color: var(--ink);
  }
  .website {
    position: absolute;
    left: 0;
    width: 1200px;
    top: 655px;
    text-align: center;
    font-weight: 700;
    font-size: 28px;
    letter-spacing: 3px;
    color: var(--earth-brown);
  }
</style>
</head>
<body>
  <main class="card">
    <svg class="card__wave" viewBox="0 0 1045 638" preserveAspectRatio="none" aria-hidden="true">
      <path d="M515,0 L1045,0 L1045,638 L760,638 C860,600 960,540 1000,470 C1040,410 1046,360 1040,320 C1030,250 990,200 960,150 C930,90 900,35 850,22 C780,15 700,30 640,25 C590,20 550,10 515,0 Z"/>
    </svg>

    <header class="brand">
      <span class="brand__mark" aria-hidden="true"></span>
      <h1 class="brand__name">
        <span class="brand__name-main">Brightwater</span>
        <span class="brand__name-sub">Cleaning Service</span>
      </h1>
    </header>

    <section class="person">
      <p class="person__name">LLC Marco Villanueva</p>
      <p class="person__role">Owner</p>
    </section>

    <div class="divider" aria-hidden="true"></div>

    <ul class="contact">
      <li>Cell 555-318-7724</li>
      <li>Office 555-374-6082</li>
      <li>marco@brightwatercleaningservice.example</li>
    </ul>

    <p class="tagline">As a leading provider of cleaning service</p>
    <p class="website">brightwatercleaningservice.example</p>
  </main>
</body>
</html>
```